Wordpress Design Project - New Website for Catering Company

Thimble Hearth Catering is looking for a new and improved website to sell its Private Catering Service to London and S.E based businesses and private clients. Our current website www.thimbleuk-example.co.uk details our offerings, but it is rather plain currently and we would like something much more image focused. Attached is also our new logo.

We would like to include lots of images of lovely food (canapés, dinners, artisan breads, yummy cheeses, fresh ingredients, cakes, brownies etc) to show we are high-end chefs that produce delicious, fresh and seasonal food. We have some stock images that we have taken and own, but we are also interested in using stock photography from elsewhere. Some other catering and food websites that we like are….

www.harrowandfinch-example.com (we like the use of images on this site and the simple layout and navigation)
www.bluekettlecatering-example.co.uk (we like the use of images to illustrate the services offered)
http://www.oatandembertable-example.com/index.php?option=com_content&view=frontpage&Itemid=1 (again an image based site that we like. We also want to incorporate a 'seasonal recipe' section that we can update regularly and easily
http://marvas-larder-example.co.uk/ (we also quite like the idea of rotating images on the home page, like this site. We also like the idea of a 'less is more' homepage, that isn't overloaded with info
http://www.thebrinetable-example.com/ (we like the simple homepage on this one)

We would like the menu to run as follows…..

1) Homepage (image lead, basic info about us, quick link to seasonal recipe)

2) Services
2.1 Canapes
2.2 Working Lunches
2.3 Dinner Parties
2.4 Fork buffets
2.5 Food for Children
2.6 Celebrations (Wedding / Christenings)
2.7 Freezer Filling / Drop off Dinners
2.8 Hampers and Food Gifts
2.9 Wine Matching & Drinks

3) Staff

4) Menus
4.1 Spring/Summer Canape Menu
4.2 Autumn/Winter Canape Menu
4.3 Spring/Summer Buffet Menu
4.4 Autumn/Winter Buffet Menu
4.5 Spring/Summer Dinner Party Menu
4.6 Autumn/Winter Dinner Party Menu
4.7 Wine List

5) Seasonal Recipe

6) Testimonials & Clients

7) About us & Contact Details

We would also like to be able to update the seasonal recipe page easily and potentially also turn this in to a mail shot which we can send to clients - we'd like this integrated in to the CMS.

We currently have a twitter account - thimble cooks and a Facebook page (Thimble Hearth Catering) which we would also like to integrate in to the website.

We would like a word press or joomla site which we are able to manage easily.

Reason: I think the sites that have come through are a good start, but we are looking for something a little more high-end I think - particularly with regards to the food images used on the site.

Target Market(s)

London based companies wanting high-end catering e.g marketing agencies, lawyers, financial industries. Also private clients wanting parties

Industry/Entity Type

Catering

Requirements
Must have
• Link to our twitter and Facebook account.

Seasonal recipe page that is easy for us to update (we aren't technical at all!)

```html
<!DOCTYPE html>
<html lang="en">
<head>
<meta charset="utf-8">
<title>Thimble Hearth Catering – Menus</title>
<link href="https://fonts.googleapis.com/css2?family=Arimo:wght@400;700&display=swap" rel="stylesheet">
<style>
  :root {
    --lavender: #d8c5d4;
    --plum-dark: #4a1740;
    --plum-band: #6b2a5c;
    --mauve: #8c6f86;
    --panel: #ffffff;
    --rule: #e2e2e2;
    --card: #1c1c1c;
    --card-text: #f2f2f2;
    --nav-text: #3a1032;
    --nav-active: #8a1e2e;
    --brand-green: #8cc63f;
    --select-bg: #4a1a44;
  }
  * { margin: 0; padding: 0; box-sizing: border-box; }
  html, body { width: 1200px; height: 1200px; overflow: hidden; }
  body {
    position: relative;
    font-family: "Arimo", Arial, sans-serif;
    background: linear-gradient(to bottom,
      var(--lavender) 0 190px,
      var(--plum-band) 190px,
      var(--plum-dark) 302px,
      var(--plum-dark) 480px,
      var(--mauve) 480px);
  }
  .site-nav {
    position: absolute; left: 67px; top: 0; height: 67px;
    display: flex;
    border-left: 1px solid var(--nav-text);
  }
  .site-nav a {
    display: flex; align-items: center;
    padding: 0 11px;
    font-size: 12px; text-transform: uppercase;
    color: var(--nav-text); text-decoration: none;
    border-right: 1px solid var(--nav-text);
  }
  .site-nav a.current { color: var(--nav-active); }
  .brand {
    position: absolute; left: 172px; top: 150px;
    font-size: 38px; font-weight: 700;
    color: var(--brand-green);
    white-space: nowrap;
  }
  .cutlery {
    position: absolute; left: 670px; top: 90px;
    width: 260px; height: 200px;
  }
  .category-select {
    position: absolute; left: 916px; top: 105px;
    width: 214px; height: 42px;
    background: var(--select-bg);
    border: 1px solid #2a0b26;
    display: flex; align-items: center; justify-content: space-between;
    padding-left: 10px;
    color: #fff; font-size: 13px; text-transform: uppercase; letter-spacing: 0.5px;
  }
  .category-select .arrow-btn {
    width: 38px; height: 38px; margin-right: 1px;
    background: #9a9a9a;
    display: flex; align-items: center; justify-content: center;
  }
  .content-panel {
    position: absolute; left: 56px; top: 302px;
    width: 1095px; height: 898px;
    background: var(--panel);
  }
  .page-title {
    position: absolute; left: 20px; top: 26px;
    font-size: 29px; font-weight: 700; color: #111;
  }
  .title-rule, .bottom-rule {
    position: absolute; left: 20px; right: 20px; height: 2px; background: var(--rule);
  }
  .title-rule { top: 71px; }
  .bottom-rule { top: 811px; }
  .menu-card {
    position: absolute; top: 96px;
    width: 246px; height: 693px;
    background: var(--card);
    overflow: hidden;
  }
  .menu-card .photo { display: block; width: 246px; height: 168px; }
  .menu-card h2 {
    padding: 16px 12px 0;
    font-size: 26px; line-height: 1.1; font-weight: 700; color: #fff;
  }
  .menu-card p {
    padding: 14px 12px 0;
    font-size: 18px; line-height: 26px; color: var(--card-text);
  }
</style>
</head>
<body>
  <nav class="site-nav">
    <a class="current" href="#">Home</a>
    <a href="#">Sample Page</a>
    <a href="#">About Thimble</a>
    <a href="#">Services</a>
    <a href="#">Staff</a>
    <a href="#">Recipes</a>
    <a href="#">Testimonials</a>
  </nav>

  <div class="brand">Thimble Hearth Catering</div>

  <svg class="cutlery" role="img" aria-label="Faint silhouettes of a spoon, fork and knife" viewBox="0 0 260 200">
    <defs>
      <linearGradient id="cutleryTone" x1="0" y1="0" x2="0" y2="1">
        <stop offset="0" stop-color="#c4aebf" stop-opacity="0.35"/>
        <stop offset="1" stop-color="#7a3c6c" stop-opacity="0.3"/>
      </linearGradient>
    </defs>
    <rect width="260" height="200" fill="url(#cutleryTone)"/>
  </svg>

  <div class="category-select">
    <span>Select a Category</span>
    <span class="arrow-btn">
      <svg width="16" height="10" viewBox="0 0 16 10"><path d="M0 0h16L8 10z" fill="#222"/></svg>
    </span>
  </div>

  <main class="content-panel">
    <h1 class="page-title">Menus</h1>
    <div class="title-rule"></div>

    <article class="menu-card" style="left:20px">
      <svg class="photo" role="img" aria-label="Plated lunch dishes lined up on a pass" viewBox="0 0 246 168">
        <defs><linearGradient id="ph1" x1="0" y1="0" x2="0" y2="1"><stop offset="0" stop-color="#3a2a22"/><stop offset="1" stop-color="#d9d2c8"/></linearGradient></defs>
        <rect width="246" height="168" fill="url(#ph1)"/>
      </svg>
      <h2>Spring Lunch/Dinner Menu</h2>
      <p>Starter Salad of seared salmon, quails egg, green mango and mint Pan fried scallops with horseradish cream and samphire (substituted for rocket out of season) Leek, bacon and blue cheese tart served with a rocket salad Coarse terrine of pork and sage served with rhubarb chutney and walnut bread Lentil and chorizo soup with basil […]</p>
    </article>

    <article class="menu-card" style="left:288px">
      <svg class="photo" role="img" aria-label="Guests serving themselves from a buffet table" viewBox="0 0 246 168">
        <defs><linearGradient id="ph2" x1="0" y1="0" x2="0" y2="1"><stop offset="0" stop-color="#5a3a28"/><stop offset="1" stop-color="#c9a27a"/></linearGradient></defs>
        <rect width="246" height="168" fill="url(#ph2)"/>
      </svg>
      <h2>Buffet Menu</h2>
      <p>Served Cold Roasted butternut squash, pomegranate and chickpea salad Roast aubergine with saffron yoghurt and pomegranate Fresh pesto rice salad with slow roasted cherry tomatoes and parmesan shavings Puy lentils with sour cherries, bacon and gorgonzola Tarts – warm or cold Puff pastry tart with sautéed portabella mushrooms, tarragon, caramelised onions and goat’s cheese Puff […]</p>
    </article>

    <article class="menu-card" style="left:556px">
      <svg class="photo" role="img" aria-label="Rows of plated canapés on a kitchen counter" viewBox="0 0 246 168">
        <defs><linearGradient id="ph3" x1="0" y1="0" x2="0" y2="1"><stop offset="0" stop-color="#3a2a22"/><stop offset="1" stop-color="#dcd4ca"/></linearGradient></defs>
        <rect width="246" height="168" fill="url(#ph3)"/>
      </svg>
      <h2>Spring Canapé Menu</h2>
      <p>Spring Canapé Menu Canapé platters will be decorated with miniature bouquets of flowers Served Cold Seared tuna in a white and black sesame coating served with micro basil garnish Aberdeen Angus fillet carpaccio with lime mascapone and rocket crostini Beetroot gradvalax with horseradish crème fraîche on rye bread Pineapple and Fenmoor Crumbly on skewers (v) […]</p>
    </article>

    <article class="menu-card" style="left:825px">
      <svg class="photo" role="img" aria-label="Table laid with white linen, glasses and lilac flowers" viewBox="0 0 246 168">
        <defs><linearGradient id="ph4" x1="0" y1="0" x2="1" y2="1"><stop offset="0" stop-color="#eeeaf0"/><stop offset="0.6" stop-color="#b8a6c4"/><stop offset="1" stop-color="#e4dfe6"/></linearGradient></defs>
        <rect width="246" height="168" fill="url(#ph4)"/>
      </svg>
      <h2>Menus</h2>
      <p>We tailor our menus throughout the year to make the most of seasonally available ingredients. Click through our sample menus for ideas; these are just a few examples of canapes and dishes we can provide.</p>
    </article>

    <div class="bottom-rule"></div>
  </main>
</body>
</html>
```